Business Card for Web Design consulting firm

Business card designs for Web Design consulting firm

Target Market(s)

English speaking adults ages 30 - 60. Predominantly professional services eg. Doctor, Dentist

Industry/Entity Type

Consulting

Requirements
Must have
• Double sided card

```html
<!DOCTYPE html>
<html lang="en">
<head>
<meta charset="utf-8">
<title>Ventaro Business Card</title>
<link rel="stylesheet" href="https://fonts.googleapis.com/css2?family=Michroma&family=Orbitron:wght@500&display=swap">
<style>
  :root {
    --stage: #000000;
    --paper: #ffffff;
    --orange: #f39a1f;
    --charcoal: #4b4b4b;
    --ink: #5a5a5a;
    --light: #f2f2f2;
  }
  html, body {
    margin: 0;
    padding: 0;
    width: 1200px;
    height: 899px;
    overflow: hidden;
    background: var(--stage);
  }
  .canvas {
    position: relative;
    width: 1200px;
    height: 899px;
    background: var(--stage);
  }
  .card {
    position: absolute;
    left: 338px;
    width: 629px;
  }
  .card-front {
    top: 32px;
    height: 404px;
    background: var(--paper);
  }
  .brand {
    position: absolute;
    left: 0;
    right: 0;
    top: 128px;
    display: flex;
    flex-direction: column;
    align-items: center;
  }
  .brand-mark {
    width: 70px;
    height: 70px;
    background: var(--orange);
    margin-bottom: 34px;
  }
  .brand-name {
    font-family: "Michroma", sans-serif;
    font-size: 50px;
    letter-spacing: 6px;
    color: var(--ink);
    line-height: 1;
  }
  .card-back {
    top: 468px;
    height: 407px;
    background: var(--charcoal);
  }
  .back-band {
    height: 169px;
    background: var(--orange);
  }
  .contact {
    position: absolute;
    top: 195px;
    font-family: "Orbitron", sans-serif;
    font-weight: 500;
    font-size: 14px;
    line-height: 23.7px;
    letter-spacing: 1.2px;
    color: var(--light);
    text-transform: uppercase;
    margin: 0;
    font-style: normal;
  }
  .contact-person { left: 48px; }
  .contact-lines { left: 317px; }
  .contact span { display: block; white-space: nowrap; }
</style>
</head>
<body>
<main class="canvas">
  <section class="card card-front" aria-label="Card front">
    <div class="brand">
      <div class="brand-mark"></div>
      <div class="brand-name">VENTARO</div>
    </div>
  </section>
  <section class="card card-back" aria-label="Card back">
    <div class="back-band"></div>
    <address class="contact contact-person">
      <span>Sam Carter</span>
      <span>Managing Director</span>
      <span>45 Harbour Lane</span>
      <span>Sydney &nbsp; NSW &nbsp; 2000</span>
      <span>Australia</span>
    </address>
    <address class="contact contact-lines">
      <span>Tel: 02 5550 1234</span>
      <span>Fax: 02 5550 1233</span>
      <span>Mob: 0400 555 789</span>
      <span>Email: sam@ventaro.com.au</span>
      <span>Web: www.ventaro.com.au</span>
    </address>
  </section>
</main>
</body>
</html>
```